I need a direct mail postcard made up for my marketing campaign

I am starting a marketing campaign and need a design for a post card. I own an iron door company and need to have before and after images on the post card to showcase what our work looks like. I have provided pictures to use below.

The design needs to be two sided. The logo should be on the front.

The tag line for this campaign is: Design the smile your home deserves.

Words to also use: Distinctive style, Work of Art, One-of-a-Kind, Elegant, Modern, Innovative, Unique

My information for the card
Name: Dean Harlowe
Phone number: (555)-318-2764
Email: Dean@wroughtgatestudio.example

The US postal system is very picky as to what can be sent in the mail. The only requirement they have is for the address. There needs to be a 2inch (50.8mm) by 4inch (101.6mm) blank space on the bottom right hand corner on the back of the card.

Target Market(s)

Home owners

Industry/Entity Type

Home Improvement

Font styles to use
Serif
Decorative

Colors
0555a3
ffffff
ec1f27

Requirements
Must have
• My logo, My contact information, before and after pictures
• Provided 3D images
Nice to have
• Words that describe iron doors
• A contrast between contemporary and ornate doors.

```html
<!DOCTYPE html>
<html lang="en">
<head>
<meta charset="utf-8">
<title>Wrought Gate Studio – Postcard</title>
<link href="https://fonts.googleapis.com/css2?family=Ultra&family=Open+Sans:wght@600;800&family=Yellowtail&family=Dancing+Script:wght@500&display=swap" rel="stylesheet">
<style>
:root{
  --blue:#0555a3;
  --red:#ec1f27;
  --white:#ffffff;
  --paper:#f4f4f6;
  --stage:#1c2420;
}
*{box-sizing:border-box;margin:0;padding:0}
html,body{width:1200px;height:1200px;overflow:hidden;background:var(--stage)}
.card{position:absolute;left:120px;width:960px;height:540px;background:var(--white);overflow:hidden;box-shadow:0 10px 30px rgba(0,0,0,.5)}
.card--front{top:40px;background:var(--paper)}
.card--back{top:620px}

/* front */
.render{position:absolute;box-shadow:0 6px 14px rgba(0,0,0,.15)}
.render--classic{left:40px;top:28px;width:300px;height:400px;background:radial-gradient(ellipse at 55% 45%,#6b3d1c 0 38%,#e2e2e4 62%)}
.render--modern{left:630px;top:28px;width:290px;height:360px;background:radial-gradient(ellipse at 50% 48%,#5a3216 0 40%,#e4e4e6 64%)}
.qualities{position:absolute;left:340px;top:20px;width:280px;list-style:none;text-align:center;font-family:"Ultra",serif;font-size:25px;line-height:42px;white-space:nowrap}
.qualities li:nth-child(odd){color:var(--blue)}
.qualities li:nth-child(even){color:var(--red)}
.band{position:absolute;left:0;top:400px;width:960px;height:110px;background:var(--blue)}
.strip{position:absolute;left:0;top:510px;width:960px;height:30px;background:var(--red);z-index:3}
.tagline{position:absolute;left:45px;top:418px;color:var(--white);font-family:"Yellowtail",cursive;font-size:36px;line-height:44px;z-index:2}
.tagline span{display:block}
.logo{position:absolute;left:380px;top:342px;width:180px;height:180px;border-radius:50%;background:var(--blue);z-index:2;display:flex;align-items:center;justify-content:center;gap:8px}
.logo__dot{width:12px;height:12px;border:2px solid var(--white);border-radius:50%}
.logo__name{color:var(--white);font-family:"Open Sans",sans-serif;font-weight:600;font-size:16px;line-height:20px;text-align:center;letter-spacing:1px}
.portrait{position:absolute;border-radius:50%;border:4px solid var(--white);background:linear-gradient(160deg,#c9ced3,#8a8f96)}
.card--front .portrait{left:640px;top:408px;width:94px;height:94px;z-index:2}
.name-pill{position:absolute;left:705px;top:398px;width:230px;height:38px;border-radius:0 19px 19px 0;background:var(--red);color:var(--white);font-family:"Open Sans",sans-serif;font-weight:800;font-size:22px;line-height:38px;padding-left:40px;white-space:nowrap}
.contact-line{position:absolute;color:var(--white);display:flex;align-items:center;gap:8px;white-space:nowrap}
.contact-line svg{fill:var(--white);flex:none}
.phone{font-family:"Open Sans",sans-serif;font-weight:800}
.email{font-family:"Dancing Script",cursive;font-weight:500}
.card--front .phone{left:748px;top:444px;font-size:16px}
.card--front .email{left:742px;top:470px;font-size:14px;gap:6px}

/* back */
.compare{position:absolute;background:var(--blue)}
.compare--one{left:40px;top:60px;width:340px;height:310px}
.compare--two{left:395px;top:50px;width:330px;height:310px}
.tab{position:absolute;top:-26px;height:40px;background:var(--red);color:var(--white);font-family:"Open Sans",sans-serif;font-weight:800;font-size:20px;line-height:40px;text-align:center;border-radius:14px 14px 0 0}
.shot{position:absolute;border:4px solid var(--white);box-shadow:0 4px 8px rgba(0,0,0,.3)}
.contact-band{position:absolute;left:0;top:385px;width:545px;height:125px;background:var(--red)}
.card--back .portrait{left:40px;top:388px;width:132px;height:132px;z-index:2}
.name-tab{position:absolute;left:200px;top:358px;width:280px;height:52px;background:var(--blue);border-radius:26px 26px 0 0;color:var(--white);font-family:"Open Sans",sans-serif;font-weight:800;font-size:27px;line-height:52px;text-align:center;z-index:2}
.card--back .phone{left:220px;top:425px;font-size:24px}
.card--back .email{left:220px;top:462px;font-size:19px}
</style>
</head>
<body>

<section class="card card--front" aria-label="Postcard front">
  <div class="render render--classic" role="img" aria-label="3D render of an ornate double iron door with sweeping curved bars"></div>
  <ul class="qualities">
    <li>Distinctive style</li>
    <li>Work of Art</li>
    <li>One-of-a-Kind</li>
    <li>Elegant</li>
    <li>Modern</li>
    <li>Innovative</li>
    <li>Unique</li>
  </ul>
  <div class="render render--modern" role="img" aria-label="3D render of a modern iron door with horizontal bars and sidelights"></div>

  <div class="band"></div>
  <p class="tagline"><span>Design the Smile</span><span>Your Home Deserves</span></p>
  <div class="logo"><span class="logo__dot"></span><span class="logo__name">WROUGHT GATE<br>STUDIO</span></div>
  <div class="portrait" role="img" aria-label="Portrait photo of Dean Harlowe"></div>
  <div class="name-pill">Dean Harlowe</div>
  <p class="contact-line phone"><svg width="15" height="15" viewBox="0 0 24 24"><path d="M6.6 10.8a15.1 15.1 0 0 0 6.6 6.6l2.2-2.2c.3-.3.7-.4 1-.2 1.1.4 2.3.6 3.6.6.6 0 1 .4 1 1V20c0 .6-.4 1-1 1A17 17 0 0 1 3 4c0-.6.4-1 1-1h3.5c.6 0 1 .4 1 1 0 1.3.2 2.5.6 3.6.1.3 0 .7-.2 1z"/></svg>(555)-318-2764</p>
  <p class="contact-line email"><svg width="14" height="11" viewBox="0 0 24 18"><path d="M0 0h24v18H0zM2 2v.5l10 7 10-7V2zm0 3v11h20V5l-10 7z"/></svg>Dean@wroughtgatestudio.example</p>
  <div class="strip"></div>
</section>

<section class="card card--back" aria-label="Postcard back">
  <div class="compare compare--one">
    <div class="tab" style="left:10px;width:140px">BEFORE</div>
    <div class="tab" style="left:180px;width:140px">AFTER</div>
    <div class="shot" style="left:15px;top:28px;width:145px;height:265px;background:linear-gradient(160deg,#8a4a26,#4f2713)" role="img" aria-label="Before photo: worn wooden double door"></div>
    <div class="shot" style="left:168px;top:18px;width:160px;height:275px;background:radial-gradient(ellipse at 50% 40%,#b08a3a,#1c1a24 70%)" role="img" aria-label="After photo: black wrought iron double door with scroll glass"></div>
  </div>
  <div class="compare compare--two">
    <div class="tab" style="left:10px;width:130px">BEFORE</div>
    <div class="tab" style="left:175px;width:140px">AFTER</div>
    <div class="shot" style="left:15px;top:40px;width:135px;height:255px;background:linear-gradient(#5a4630 0 20%,#f2f2f0 22%)" role="img" aria-label="Before photo: white paneled double door with fanlight"></div>
    <div class="shot" style="left:165px;top:30px;width:150px;height:265px;border-radius:75px 75px 0 0;background:linear-gradient(#3a3548,#2a2636)" role="img" aria-label="After photo: arched iron double door with holiday wreaths"></div>
  </div>

  <div class="contact-band"></div>
  <div class="portrait" role="img" aria-label="Portrait photo of Dean Harlowe"></div>
  <div class="name-tab">Dean Harlowe</div>
  <p class="contact-line phone"><svg width="20" height="20" viewBox="0 0 24 24"><path d="M6.6 10.8a15.1 15.1 0 0 0 6.6 6.6l2.2-2.2c.3-.3.7-.4 1-.2 1.1.4 2.3.6 3.6.6.6 0 1 .4 1 1V20c0 .6-.4 1-1 1A17 17 0 0 1 3 4c0-.6.4-1 1-1h3.5c.6 0 1 .4 1 1 0 1.3.2 2.5.6 3.6.1.3 0 .7-.2 1z"/></svg>(555)-318-2764</p>
  <p class="contact-line email"><svg width="22" height="16" viewBox="0 0 24 18"><path d="M0 0h24v18H0zM2 2v.5l10 7 10-7V2zm0 3v11h20V5l-10 7z"/></svg>Dean@wroughtgatestudio.example</p>
</section>

</body>
</html>
```